"Velour Balm" Brand of All Natural Body Butter needs beautiful packaging design

I make body butters brought up from exotic destinations in South East Asia and South America. All natural Vegan (even preservative is edible). This body butter can be used even on face. Great even for sensitive skin.

I have very sensitive skin and i started finding a product that would fit my complexion. Didn't find much on the market so I started doing research and came up with my own recipe that makes my skin silky and amazing. This product means a lot to me and it's time to giving it up to the world.

I have many variaties of smells made out of 100% natural essential oils

Target Market(s)

Mostly women and also I offer products for men (fragrance free)

Font styles to use
Decorative
Script

Colors

Designer to choose colors to be used in the design.

Requirements
Must have
• Has to be a very stylish design, sophisticated touch, you see the packaging and you want to see what it is
Nice to have
• i want to look very attractive to both young and older audience
Should not have
• cheezy regular over the counter lotion design

```html
<!DOCTYPE html>
<html lang="en">
<head>
<meta charset="utf-8">
<title>Velour Balm – Lid Label</title>
<link rel="stylesheet" href="https://fonts.googleapis.com/css2?family=Quicksand:wght@300;500&family=Quattrocento:wght@400&display=swap">
<style>
  :root {
    --paper: #ffffff;
    --cream: #fdfdf1;
    --mint: #e4f2ee;
    --leaf: #cfe3c8;
    --blossom: #fbe2cf;
    --rose: #f6d3cc;
    --sky: #dde9f5;
    --ink: #1e0a0a;
    --accent-blue: #a8d8ea;
    --coral: #f07a62;
  }
  * { box-sizing: border-box; margin: 0; padding: 0; }
  html, body {
    width: 1200px;
    height: 1200px;
    overflow: hidden;
    background: var(--paper);
  }
  .label-canvas {
    position: relative;
    width: 1200px;
    height: 1200px;
  }
  .label-disc {
    position: absolute;
    left: 44px;
    top: 40px;
    width: 1116px;
    height: 1116px;
    border-radius: 50%;
    overflow: hidden;
    background:
      radial-gradient(circle at 34% 16%, var(--blossom) 0%, rgba(251,226,207,0) 20%),
      radial-gradient(circle at 18% 26%, var(--rose) 0%, rgba(246,211,204,0) 13%),
      radial-gradient(circle at 50% 9%, var(--leaf) 0%, rgba(207,227,200,0) 13%),
      radial-gradient(circle at 80% 30%, var(--leaf) 0%, rgba(207,227,200,0) 22%),
      radial-gradient(circle at 88% 67%, var(--sky) 0%, rgba(221,233,245,0) 18%),
      radial-gradient(circle at 20% 84%, var(--leaf) 0%, rgba(207,227,200,0) 17%),
      radial-gradient(circle at 76% 88%, var(--leaf) 0%, rgba(207,227,200,0) 13%),
      radial-gradient(circle at 8% 58%, var(--rose) 0%, rgba(246,211,204,0) 9%),
      radial-gradient(circle at 94% 50%, var(--rose) 0%, rgba(246,211,204,0) 9%),
      linear-gradient(160deg, var(--cream) 0%, var(--mint) 55%, var(--cream) 100%);
  }
  .brand-lockup {
    position: absolute;
    left: 0;
    right: 0;
    top: 500px;
    display: flex;
    align-items: center;
    justify-content: center;
    gap: 26px;
  }
  .brand-dot {
    width: 56px;
    height: 56px;
    border-radius: 50%;
    background: var(--accent-blue);
  }
  .brand-name {
    font-family: "Quicksand", sans-serif;
    font-weight: 500;
    font-size: 150px;
    line-height: 1;
    color: var(--ink);
    letter-spacing: 1px;
  }
  .product-info {
    position: absolute;
    left: 0;
    right: 0;
    top: 888px;
    text-align: center;
    color: var(--coral);
  }
  .product-claim {
    font-family: "Quicksand", sans-serif;
    font-weight: 300;
    font-size: 66px;
    line-height: 1;
  }
  .product-use {
    font-family: "Quattrocento", serif;
    font-size: 40px;
    line-height: 1;
    margin-top: 8px;
    letter-spacing: 1px;
  }
  .product-weight {
    font-family: "Quattrocento", serif;
    font-size: 36px;
    line-height: 1;
    margin-top: 16px;
    letter-spacing: 2px;
  }
</style>
</head>
<body>
  <main class="label-canvas">
    <div class="label-disc" role="img" aria-label="Soft watercolour background of tropical palm fronds, monstera leaves, peach hibiscus flowers and coral berry sprigs"></div>

    <div class="brand-lockup">
      <span class="brand-dot"></span>
      <h1 class="brand-name">Velour Balm</h1>
    </div>

    <div class="product-info">
      <p class="product-claim">All Natural Vegan</p>
      <p class="product-use">for all type of skin</p>
      <p class="product-weight">NET WT. 198g</p>
    </div>
  </main>
</body>
</html>
```